Tess Marlowe Communication business card

I am starting a small, country-based business that offers writing, communication and marketing services to a wide range of clients, inner city big business, to mining, through to agriculture.

The appeal of my business is that it's mobile and flexible. It's just me, with lots of hands-on experience on construction and infrastructure projects.

I can provide the following services:

• Communication planning and management
• Issues and media management
• Marketing and communication materials
• Project management and strategy
• Government liaison
• Incident management communication
• Stakeholder management

It would be great to be able to use the elements of the business card design on other stationery.

Industry/Entity Type

Communication

Requirements
Must have
• The following information:

Tess Marlowe
M: 0427 391 864
E: tess@tmcommsmail.com

PO Box 152
Durrandale Q 4472
Nice to have
• a rural element (windmill, workboots, wheat stalk)

```html
<!DOCTYPE html>
<html lang="en">
<head>
<meta charset="UTF-8">
<title>Tess Marlowe Communication – Business Card</title>
<link rel="stylesheet" href="https://fonts.googleapis.com/css2?family=Exo+2:wght@400;600&display=swap">
<style>
  :root {
    --olive: #6a7433;
    --leaf: #c9dc87;
    --rust: #c8392b;
    --paper: #ffffff;
    --ink: #1e1e1e;
    --backdrop: #3a3a3a;
    --font: "Exo 2", sans-serif;
  }
  * { box-sizing: border-box; margin: 0; padding: 0; }
  html, body {
    width: 1200px; height: 900px; overflow: hidden;
    background: var(--backdrop);
    font-family: var(--font);
  }
  .canvas {
    width: 1200px; height: 900px;
    display: flex; flex-direction: column;
    align-items: center; justify-content: center; gap: 34px;
  }
  .card {
    position: relative;
    width: 700px; height: 400px;
    overflow: hidden;
    box-shadow: 0 6px 18px rgba(0,0,0,.35);
  }

  /* Shared brand lockup */
  .brand {
    position: absolute;
    display: flex; align-items: center; gap: 12px;
  }
  .brand__dot { flex: none; border-radius: 50%; background: var(--leaf); }
  .brand__name { font-weight: 600; line-height: 1.2; }

  /* Front */
  .card--front { background: var(--paper); }
  .card__wave { position: absolute; inset: 0; width: 100%; height: 100%; }
  .card--front .brand { left: 26px; top: 62px; width: 200px; }
  .card--front .brand__dot { width: 40px; height: 40px; }
  .card--front .brand__name { color: var(--olive); font-size: 17px; }
  .holder-name {
    position: absolute; left: 236px; top: 40px;
    font-size: 26px; font-weight: 400; color: var(--ink);
  }
  .contact {
    position: absolute; left: 320px; top: 94px;
    font-style: normal; font-size: 20px; line-height: 1.3; color: var(--ink);
  }
  .card--front .web {
    position: absolute; left: 24px; bottom: 22px;
    font-size: 20px; color: var(--paper);
  }

  /* Back */
  .card--back { background: var(--olive); color: var(--paper); }
  .card--back .brand { left: 0; right: 0; top: 62px; justify-content: center; }
  .card--back .brand__dot { width: 52px; height: 52px; }
  .card--back .brand__name { color: var(--leaf); font-size: 24px; }
  .services {
    position: absolute; left: 40px; right: 30px; top: 196px;
    display: grid;
    grid-template-columns: auto auto;
    justify-content: space-between;
    column-gap: 24px;
    list-style: none; font-size: 15px; line-height: 22px;
    white-space: nowrap;
  }
  .services li::before { content: "\2022"; margin-right: 6px; }
  .services .col-left { grid-column: 1; }
  .services .col-right { grid-column: 2; }
  .card--back .web {
    position: absolute; left: 0; right: 0; bottom: 28px;
    text-align: center; font-size: 22px;
  }
</style>
</head>
<body>
<main class="canvas">
  <section class="card card--front" aria-label="Business card front">
    <svg class="card__wave" viewBox="0 0 700 400" preserveAspectRatio="none" aria-hidden="true">
      <path d="M0 300 C 220 312, 480 276, 700 220 L700 400 L0 400 Z" fill="var(--olive)"/>
      <path d="M0 294 C 220 306, 480 270, 700 214" fill="none" stroke="var(--leaf)" stroke-width="6"/>
      <path d="M0 286 C 220 298, 480 262, 700 206" fill="none" stroke="var(--rust)" stroke-width="3"/>
    </svg>
    <div class="brand">
      <span class="brand__dot"></span>
      <span class="brand__name">Tess Marlowe Communication</span>
    </div>
    <h1 class="holder-name">Tess Marlowe</h1>
    <address class="contact">
      PO Box 152<br>
      Durrandale Q 4472<br>
      M: 0427 391 864<br>
      E: tess@tmcommsmail.com
    </address>
    <p class="web">www.tmcommsmail.com</p>
  </section>

  <section class="card card--back" aria-label="Business card back">
    <div class="brand">
      <span class="brand__dot"></span>
      <span class="brand__name">Tess Marlowe Communication</span>
    </div>
    <ul class="services">
      <li class="col-left">Communication planning and management</li>
      <li class="col-right">Project management and strategy</li>
      <li class="col-left">Issues and media management</li>
      <li class="col-right">Government liaison</li>
      <li class="col-left">Marketing and communication materials</li>
      <li class="col-right">Incident management communication</li>
      <li class="col-right">Stakeholder management</li>
    </ul>
    <p class="web">www.tmcommsmail.com</p>
  </section>
</main>
</body>
</html>
```